Clever & creative business card needed for a pediatric dentist.

We need a business card for a pediatric dentist that is building a brand-new pediatric dental practice. He is funny, outgoing, and sociable, and he hopes to give his business card to dentists and pediatricians so that he can give them information of where to refer infants, children, and teenagers that need high quality and attainable dental care.

The name of the dental practice is Copper Fern Pediatric Dentistry. Logo design .png / .pdf/ .jpg are provided to aid in the design.

The dentist's last name is Tolvan (which sounds like "burger", as in "hamburger” or “cheeseburger"). Since it is pediatric practice, kudos will be given to designs that implement a little joke into the design - but hopefully in a small or hidden way (such as putting something like a cheeseburger on the back of the card, or hiding it an an abstract way).

Thank you!

Please make a design that incorporates colors. It should be fun! Not too serious. It does not have to follow the color scheme of the logos.

```html
<!DOCTYPE html>
<html lang="en">
<head>
<meta charset="utf-8">
<title>Copper Fern Pediatric Dentistry – Business Card</title>
<link rel="stylesheet" href="https://fonts.googleapis.com/css2?family=Quicksand:wght@500&family=Arimo:wght@400&display=swap">
<style>
  :root {
    --stage: #cccccc;
    --charcoal: #4a4544;
    --fern-green: #31995b;
    --soft-green: #b9dfb5;
    --paper: #ffffff;
    --ink: #1b1b1b;
  }
  * { margin: 0; padding: 0; box-sizing: border-box; }
  html, body { width: 849px; height: 1200px; overflow: hidden; background: var(--stage); }
  .canvas { position: relative; width: 849px; height: 1200px; background: var(--stage); }

  .card { position: absolute; width: 488px; height: 299px; border-radius: 18px; overflow: hidden; }

  /* Front */
  .card-front { left: 186px; top: 264px; background: var(--charcoal); }
  .front-mark { position: absolute; left: 50%; top: 104px; width: 48px; height: 48px; margin-left: -24px;
    border-radius: 50%; background: var(--soft-green); }
  .front-brand { position: absolute; left: 0; right: 0; top: 160px; text-align: center; color: var(--paper); }
  .brand-name { font-family: "Quicksand", sans-serif; font-weight: 500; font-size: 27px; line-height: 1; letter-spacing: 0.5px; white-space: nowrap; }
  .brand-tagline { font-family: "Quicksand", sans-serif; font-weight: 500; font-size: 8px; letter-spacing: 3px; margin-top: 5px; white-space: nowrap; }

  /* Back */
  .card-back { left: 187px; top: 594px; background: var(--paper); }
  .back-swoosh { position: absolute; left: 0; top: 0; width: 488px; height: 299px; }
  .back-band { position: absolute; left: 0; bottom: 0; width: 100%; height: 21px; background: var(--charcoal); }
  .back-mark { position: absolute; left: 100px; top: 26px; width: 40px; height: 40px; border-radius: 50%; background: var(--soft-green); }
  .back-brand { position: absolute; left: 57px; top: 80px; color: var(--charcoal); }
  .back-brand .brand-name { font-size: 21px; }
  .back-brand .brand-tagline { font-size: 7px; letter-spacing: 2.4px; margin-top: 3px; }

  .holder { position: absolute; left: 290px; top: 58px; font-family: "Arimo", sans-serif; color: var(--ink); }
  .holder-name { font-size: 22px; line-height: 1; padding-bottom: 3px; border-bottom: 1px solid var(--ink); width: 135px; white-space: nowrap; }
  .holder-role { font-size: 10px; letter-spacing: 9.2px; margin-top: 6px; white-space: nowrap; }

  .contacts { position: absolute; left: 290px; top: 171px; list-style: none; font-family: "Arimo", sans-serif; color: var(--ink); font-size: 15px; }
  .contacts li { display: flex; align-items: center; height: 21px; white-space: nowrap; }
  .contacts svg { width: 14px; height: 14px; margin-right: 9px; flex: none; }
</style>
</head>
<body>
<div class="canvas">

  <section class="card card-front">
    <span class="front-mark"></span>
    <div class="front-brand">
      <div class="brand-name">copper fern</div>
      <div class="brand-tagline">PEDIATRIC DENTISTRY</div>
    </div>
  </section>

  <section class="card card-back">
    <svg class="back-swoosh" viewBox="0 0 488 299" aria-hidden="true">
      <path d="M0 81 Q90 250 365 263 L0 263 Z" fill="var(--fern-green)"/>
    </svg>
    <div class="back-band"></div>

    <span class="back-mark"></span>
    <div class="back-brand">
      <div class="brand-name">copper fern</div>
      <div class="brand-tagline">PEDIATRIC DENTISTRY</div>
    </div>

    <div class="holder">
      <div class="holder-name">YOUR NAME</div>
      <div class="holder-role">DIRECTURE</div>
    </div>

    <ul class="contacts">
      <li>
        <svg viewBox="0 0 24 24" aria-hidden="true"><path d="M6.6 10.8c1.4 2.8 3.8 5.1 6.6 6.6l2.2-2.2c.3-.3.7-.4 1-.2 1.1.4 2.3.6 3.6.6.6 0 1 .4 1 1V20c0 .6-.4 1-1 1C10.6 21 3 13.4 3 4c0-.6.4-1 1-1h3.5c.6 0 1 .4 1 1 0 1.3.2 2.5.6 3.6.1.3 0 .7-.2 1z" fill="var(--ink)"/></svg>
        123.456.7890
      </li>
      <li>
        <svg viewBox="0 0 24 24" aria-hidden="true"><rect x="6" y="2" width="12" height="20" rx="2.5" fill="none" stroke="var(--ink)" stroke-width="2"/><circle cx="12" cy="18" r="1.2" fill="var(--ink)"/></svg>
        123.456.7890
      </li>
      <li>
        <svg viewBox="0 0 24 24" aria-hidden="true" fill="none" stroke="var(--ink)" stroke-width="1.5"><circle cx="12" cy="12" r="10"/><ellipse cx="12" cy="12" rx="4.5" ry="10"/><path d="M2 12h20M4 7h16M4 17h16"/></svg>
        www.copperfern.com
      </li>
    </ul>
  </section>

</div>
</body>
</html>
```